construction company offering modern and striking homes and apartments

I need a card design for my new construction company called Talmont Constructions (vic) Pty Ltd.
We build everything from multi home development sites to modern and edgy apartment complexes.
I am open to any colors used as long as it stands out and doesn't look cheap. I want the final design to show my prospective clients I am a professional construction company

Industry/Entity Type

Construction

```html
<!DOCTYPE html>
<html lang="en">
<head>
<meta charset="utf-8">
<title>Talmont Construction – Card</title>
<link rel="stylesheet" href="https://fonts.googleapis.com/css2?family=Crimson+Text:wght@400&display=swap">
<style>
  :root {
    --brand-red: #d50000;
    --ink-black: #000000;
    --paper: #ffffff;
  }
  html, body {
    margin: 0;
    padding: 0;
    overflow: hidden;
    background: var(--paper);
  }
  .card {
    display: block;
    width: 867px;
    height: 1200px;
    background: var(--paper);
  }
  .company-name,
  .address {
    font-family: "Crimson Text", "Times New Roman", serif;
    font-weight: 400;
    fill: var(--brand-red);
  }
  .company-name { font-size: 92px; letter-spacing: 4px; }
  .address-label { font-size: 62px; }
  .address-line { font-size: 38px; }
  .roof-block { fill: var(--ink-black); }
</style>
</head>
<body>
<svg class="card" viewBox="0 0 867 1200" width="867" height="1200" xmlns="http://www.w3.org/2000/svg">
  <g class="company-name" aria-label="Talmont Construction">
    <text x="40" y="270">TALMONT</text>
    <text x="40" y="380" textLength="780" lengthAdjust="spacingAndGlyphs">CONSTRUCTION</text>
  </g>

  <polygon class="roof-block" points="0,726 440,598 867,726 867,1200 0,1200"/>

  <g class="address">
    <text class="address-label" x="419" y="835" text-anchor="middle">Address:</text>
    <text class="address-line" x="99" y="897">27 Linden Road Ardmore vic&#160;&#160;3041</text>
  </g>
</svg>
</body>
</html>
```